Apartment Hotel
Zielgruppe
Apartment Hotel, verkauf von Hotelzimmer, bzw. Apartments. Für kurzreisende oder Langzeitaufenthalte, für Touristen , Geschäftsleuten, Firmen.
Wir stellen komplette 1 oder 2 Zimmerapartments mit Küche.
www.apartment-hotel-kornmuhlweg.de
Aufgabenstellung
modernes Logo , Briefpapier & Visitenkarten , Layout,
Platz für Name/Position: Hotelmanager

```html
<!DOCTYPE html>
<html lang="de">
<head>
<meta charset="utf-8">
<title>Apartment Hotel Kornmuhlweg – Visitenkarten</title>
<link href="https://fonts.googleapis.com/css2?family=Open+Sans:wght@300;400;600&display=swap" rel="stylesheet">
<style>
  :root {
    --backdrop: #e6e8ea;
    --card-white: #ffffff;
    --card-dark: #1f2e37;
    --ink: #3a3e42;
    --ink-soft: #6b7075;
    --rule: #b9bdc0;
    --wordmark: #5e6d76;
    --accent: #6fa3b5;
  }
  * { margin: 0; padding: 0; box-sizing: border-box; }
  html, body {
    width: 1200px; height: 900px; overflow: hidden;
    background: var(--backdrop);
    font-family: "Open Sans", Arial, sans-serif;
  }
  .canvas { position: relative; width: 1200px; height: 900px; }
  .card {
    position: absolute; left: 300px; width: 600px; height: 345px;
    overflow: hidden;
    box-shadow: 0 10px 28px rgba(0,0,0,.22);
  }
  .card--front { top: 90px; background: var(--card-white); }
  .card--back  { top: 475px; background: var(--card-dark); }

  .front-info {
    height: 200px; text-align: center; color: var(--ink);
    padding-top: 26px;
    background: linear-gradient(180deg, #fff 0%, #f1f2f3 100%);
  }
  .person-name { font-size: 24px; font-weight: 400; letter-spacing: .2px; }
  .person-role { font-size: 11px; color: var(--ink-soft); margin-top: 1px; }
  .divider {
    width: 290px; height: 1px; margin: 16px auto 14px;
    background: linear-gradient(90deg, transparent, var(--rule), transparent);
  }
  .contact { font-size: 13.5px; font-weight: 300; line-height: 19px; }

  .front-band {
    height: 145px; background: var(--card-dark);
    display: flex; align-items: center; justify-content: center;
  }
  .wordmark {
    display: flex; align-items: center; gap: 12px;
    color: var(--wordmark); font-weight: 400; text-transform: uppercase;
    letter-spacing: 3px;
  }
  .wordmark__dot { width: 10px; height: 10px; border-radius: 50%; background: var(--wordmark); }
  .front-band .wordmark { font-size: 26px; }

  .back-content {
    height: 100%; display: flex; flex-direction: column;
    align-items: center; justify-content: center; gap: 28px;
  }
  .card--back .wordmark { font-size: 40px; letter-spacing: 4px; }
  .card--back .wordmark__dot { width: 14px; height: 14px; }
  .web-address { color: var(--accent); font-size: 15px; font-weight: 400; }
</style>
</head>
<body>
<main class="canvas">
  <section class="card card--front" aria-label="Visitenkarte Vorderseite">
    <div class="front-info">
      <p class="person-name">Marlene Vogt</p>
      <p class="person-role">Hotelmanager</p>
      <div class="divider"></div>
      <p class="contact">Apartment Hotel Kornmuhlweg</p>
      <p class="contact">Hagebuttenweg 14 · 99084 Erfurt</p>
      <p class="contact">Tel. +49 361-5520417 · Fax +49 361-5520499</p>
      <p class="contact">info@hotel-kornmuhlweg.de · www.apartment-hotel-kornmuhlweg.de</p>
    </div>
    <div class="front-band">
      <div class="wordmark"><span class="wordmark__dot"></span>Kornmuhlweg</div>
    </div>
  </section>

  <section class="card card--back" aria-label="Visitenkarte Rückseite">
    <div class="back-content">
      <div class="wordmark"><span class="wordmark__dot"></span>Kornmuhlweg</div>
      <p class="web-address">www.apartment-hotel-kornmuhlweg.de</p>
    </div>
  </section>
</main>
</body>
</html>
```